Background image design

Looking for a background image design for use in a website. It should be based off the attached logo and modeled after the attached background image. Will need a second image reading "CORALVEST DASHBOARD" similar to what is displayed in the attached as a seperate image for link purposes. Incorporation of tidecrest helicopters is also an option. Adding the buttons is optional, but they must be listed as seperate images.

```html
<!DOCTYPE html>
<html lang="en">
<head>
<meta charset="utf-8">
<title>Coralvest Dashboard</title>
<link rel="stylesheet" href="https://fonts.googleapis.com/css2?family=Fira+Sans:wght@400;600&display=swap">
<style>
  :root {
    --navy-sky-top: #1d3a6b;
    --navy-sky-mid: #1a3560;
    --navy-ridge: #0f2247;
    --band: rgba(6, 14, 30, 0.72);
    --white: #ffffff;
    --button-blue: #0a3777;
    --button-text-dark: #0d3a78;
    --black: #000000;
  }
  * { box-sizing: border-box; margin: 0; padding: 0; }
  html, body { width: 1200px; height: 900px; overflow: hidden; background: var(--black); }
  body { font-family: "Fira Sans", Arial, sans-serif; position: relative; }

  .hero {
    position: absolute; left: 0; top: 0; width: 1200px; height: 600px;
    background: linear-gradient(180deg, var(--navy-sky-top) 0%, var(--navy-sky-mid) 55%, var(--navy-ridge) 78%, #0b1a38 100%);
  }
  .title-frame {
    position: absolute; left: 349px; top: 286px; width: 502px; height: 100px;
    border: 4px solid var(--white);
    display: flex; align-items: center; justify-content: center;
    color: var(--white); font-size: 31px; letter-spacing: 0.5px;
  }
  .title-frame strong { font-weight: 600; margin-right: 9px; }

  .quick-links {
    position: absolute; left: 0; top: 491px; width: 1200px; height: 109px;
    background: var(--band);
    display: flex; gap: 8px; padding: 31px 0 0 84px;
  }
  .quick-link {
    width: 200px; height: 50px; background: var(--white);
    color: var(--button-text-dark); font-weight: 600; font-size: 18px;
    display: flex; align-items: center; justify-content: center;
    border-radius: 2px;
  }
  .quick-link.is-outline {
    background: transparent; border: 1px solid var(--white); color: var(--white);
  }

  .tool-grid {
    position: absolute; left: 186px; top: 625px;
    display: grid; grid-template-columns: repeat(4, 200px);
    column-gap: 10px; row-gap: 14px;
  }
  .tool {
    height: 50px; background: var(--button-blue); color: var(--white);
    font-size: 18px; font-weight: 400;
    display: flex; align-items: center; justify-content: center; gap: 5px;
    border-radius: 1px;
  }
  .tool b { font-weight: 600; }
  .tool.is-outline {
    background: transparent; border: 2px solid var(--button-blue); color: var(--button-blue);
  }
</style>
</head>
<body>
  <div class="hero" role="img" aria-label="Dusk sky over mountain ridges with a tidecrest helicopter in flight, tinted dark blue"></div>

  <div class="title-frame"><strong>CORALVEST</strong>DASHBOARD</div>

  <nav class="quick-links">
    <div class="quick-link">P6 Policy Memos</div>
    <div class="quick-link">P6 CCIR</div>
    <div class="quick-link">Share Drive</div>
    <div class="quick-link">Phone Roster</div>
    <div class="quick-link is-outline">LRTC</div>
  </nav>

  <nav class="tool-grid">
    <div class="tool"><b>CMD</b> &amp; Staff</div>
    <div class="tool"><b>Training</b> Meeting</div>
    <div class="tool"><b>CUOPS</b></div>
    <div class="tool"><b>Schools</b></div>
    <div class="tool"><b>Reading</b> File</div>
    <div class="tool"><b>DTMS</b></div>
    <div class="tool"><b>SAAR</b> Turn-In</div>
    <div class="tool"><b>Flight</b> Schedule</div>
    <div class="tool"><b>Flight</b> OPS</div>
    <div class="tool"><b>DTS</b></div>
    <div class="tool"><b>BNGMM</b></div>
    <div class="tool is-outline"><b>Webmail</b></div>
    <div class="tool"><b>Heron Phone</b> Roster</div>
    <div class="tool"><b>4187's</b></div>
    <div class="tool"><b>Tasking</b> Tracker</div>
    <div class="tool"><b>A/C</b> Maintenance</div>
  </nav>
</body>
</html>
```